Varen Psychiatry (Psychiatry clinic offering cutting edge treatments)

2 sided flyer for new psychiatry practice in Boulder, CO. I want something that looks professional, cutting edge, but also welcoming and friendly. My logo and pictures are attached.

Some of the copy:
Personalized, holistic Psychiatry combined with cutting-edge, evidence-based treatments. Our personalized psychiatry plan includes a bio-psycho-social evaluation, personalized treatment plan, medical evaluation for underlying hormonal and electrolyte abnormalities, and genetic testing (when warranted).

We specialize in treatment-resistant depression and substance abuse. We also treat PTSD, Bipolar Disorder, OCD, anxiety disorders, ADHD, and psychotic disorders.

About Dr. Pim- Dr. Pim served as Chief Resident at the largest private psychiatry hospital in Colorado. While there he won 3 consecutive awards for exceptionally high Psychiatry in service test score (99th percentile). He was a board member of Westfield Psychiatric Guild and helped advocate for better Colorado mental health policy. Dr. Pim is uniquely trained in Ketamine, Transcranial Magnetic Stimulation, and integrative psychiatry.

Target Market(s)

Private pay mental health patients, planning to give out to psychologists and family practice doctors

Industry/Entity Type

Medicine/Psychiatry

Colors
0054AA
0677BA
7BADD7
CADEEF
E8F1F8
0094D4
00A9DD
6FCCEA
C7EBF8
E9F6FB
00AB8E
00BBA5
67D7C9
C6EFE9
E9F9F6

Requirements
Must have
• My logo, an about me (Dr. Tom Pim) section

```html
<!DOCTYPE html>
<html lang="en">
<head>
<meta charset="utf-8">
<title>Varen Psychiatry – Two-Sided Flyer</title>
<link href="https://fonts.googleapis.com/css2?family=Poppins:ital,wght@0,400;0,500;0,600;0,700;1,600&display=swap" rel="stylesheet">
<style>
  :root {
    --stage: #939498;
    --ink: #111111;
    --paper: #ffffff;
    --night: #000000;
    --violet: #a63ee6;
    --indigo: #5a6cf0;
    --blue: #2d8ff0;
    --cyan: #14f2f6;
    --logo-grey: #6d6e73;
    --brand-grad: linear-gradient(90deg, var(--violet) 0%, var(--blue) 55%, var(--cyan) 100%);
  }
  * { box-sizing: border-box; margin: 0; padding: 0; }
  html, body { width: 1200px; height: 851px; overflow: hidden; }
  body {
    background: var(--stage);
    font-family: "Poppins", sans-serif;
    position: relative;
  }
  .flyer {
    position: absolute;
    top: 101px;
    width: 445px;
    height: 630px;
    overflow: hidden;
  }
  .flyer--front { left: 154px; background: var(--paper); }
  .flyer--back { left: 638px; background: var(--night); color: #fff; }

  .hero-photo {
    position: absolute; left: 0; top: 0; width: 445px; height: 253px;
    background:
      radial-gradient(ellipse at 58% 0%, #f08a86 0%, rgba(240,138,134,0) 40%),
      radial-gradient(ellipse at 65% 55%, #cfd4ec 0%, rgba(160,150,200,0) 45%),
      linear-gradient(120deg, #e4e7f0 0%, #b7b4cf 45%, #6a5a92 100%);
  }
  .logo-lockup {
    position: absolute; display: flex; align-items: center; gap: 7px;
    font-family: "Poppins", sans-serif; font-weight: 600; line-height: 1;
  }
  .logo-lockup__dot { border-radius: 50%; flex: none; }
  .logo-lockup__name { letter-spacing: 0.12em; text-transform: uppercase; }
  .logo-lockup--front { left: 36px; top: 160px; color: var(--logo-grey); }
  .logo-lockup--front .logo-lockup__dot { width: 20px; height: 20px; background: var(--logo-grey); }
  .logo-lockup--front .logo-lockup__name { font-size: 16px; }

  .headline-band {
    position: absolute; left: 0; top: 253px; width: 445px; height: 101px;
    background: var(--brand-grad);
    display: flex; align-items: center; justify-content: center; text-align: center;
  }
  .headline-band h1 {
    color: #fff; font-weight: 700; font-size: 21.5px; line-height: 24px; text-transform: uppercase;
  }

  .session-photo {
    position: absolute; left: 37px; top: 379px; width: 115px; height: 159px;
    background: linear-gradient(160deg, #5c4b3c 0%, #a58b6f 45%, #e2ddd4 75%, #7b6a5a 100%);
  }
  .body-copy {
    font-size: 8.6px; line-height: 10.9px; text-align: justify;
  }
  .flyer--front .body-copy { position: absolute; left: 165px; top: 377px; width: 245px; color: var(--ink); }
  .body-copy p + p { margin-top: 11px; }
  .body-copy em { font-weight: 600; }

  .phone {
    position: absolute; font-weight: 600;
    background: linear-gradient(90deg, var(--violet), var(--blue) 60%, #1fd8f5);
    -webkit-background-clip: text; background-clip: text; color: transparent;
  }
  .flyer--front .phone { left: 0; width: 100%; text-align: center; top: 556px; font-size: 30px; line-height: 34px; }
  .web-pill {
    position: absolute; height: 13px; border-radius: 7px;
    font-size: 9px; letter-spacing: 0.22em; display: flex; align-items: center; justify-content: center;
  }
  .web-pill b { font-weight: 700; }
  .flyer--front .web-pill { left: 126px; top: 592px; width: 209px; background: #111; color: #fff; }
  .flyer--back .web-pill { left: 107px; top: 577px; width: 224px; background: #fff; color: #111; }

  .circuit-art { position: absolute; bottom: 0; width: 122px; height: 70px; }
  .circuit-art--left { left: 0; background: linear-gradient(45deg, #2a7fe0 0%, #25c6f3 60%, rgba(37,198,243,0) 100%); clip-path: polygon(0 0, 100% 100%, 0 100%); }
  .circuit-art--right { right: 0; background: linear-gradient(315deg, #2a7fe0 0%, #25c6f3 60%, rgba(37,198,243,0) 100%); clip-path: polygon(100% 0, 100% 100%, 0 100%); }

  /* back side */
  .tms-photo {
    position: absolute; left: 28px; top: 28px; width: 162px; height: 156px;
    background: linear-gradient(135deg, #dfe6ee 0%, #f3f5f7 45%, #b98562 80%, #7d5a44 100%);
  }
  .flyer--back .body-copy--intro { position: absolute; left: 205px; top: 29px; width: 213px; }
  .flyer--back .body-copy--plan { position: absolute; left: 28px; top: 199px; width: 390px; }
  .flyer--back .body-copy { line-height: 10.8px; }

  .about-card {
    position: absolute; left: 89px; top: 296px; width: 332px; height: 171px;
    border-radius: 12px; background: var(--brand-grad);
  }
  .about-card__text {
    position: absolute; left: 69px; top: 17px; width: 239px;
    font-size: 8.3px; line-height: 9.85px; text-align: justify; color: #fff;
  }
  .portrait-ring {
    position: absolute; left: 16px; top: 314px; width: 138px; height: 138px;
    border-radius: 50%; background: var(--night);
    display: flex; align-items: center; justify-content: center;
  }
  .portrait {
    width: 124px; height: 124px; border-radius: 50%;
    background: radial-gradient(circle at 45% 40%, #d8d8d8 0%, #8e8e8e 60%, #3e3e3e 100%);
  }
  .logo-lockup--back { left: 118px; top: 500px; color: #fff; }
  .logo-lockup--back .logo-lockup__dot { width: 34px; height: 34px; background: #fff; }
  .logo-lockup--back .logo-lockup__name { font-size: 22px; }
  .flyer--back .phone { left: 0; width: 100%; text-align: center; top: 547px; font-size: 19px; line-height: 24px; font-weight: 500; }
  .flyer--back .phone b { font-weight: 700; }
</style>
</head>
<body>

<section class="flyer flyer--front">
  <div class="hero-photo" role="img" aria-label="Woman in profile with eyes closed and a glowing translucent brain overlay"></div>
  <div class="logo-lockup logo-lockup--front">
    <span class="logo-lockup__dot"></span>
    <span class="logo-lockup__name">Varen Psychiatry</span>
  </div>

  <div class="headline-band">
    <h1>Varen Psychiatry is<br>now accepting new patients<br>in Boulder, Colorado!</h1>
  </div>

  <div class="session-photo" role="img" aria-label="Therapist and patient talking in a bright office with plants"></div>
  <div class="body-copy">
    <p><em>We specialize in</em> treating patients with treatment resistant depression and substance abuse disorders who have not responded to other forms of treatment. We also treat patients with PTSD, Bipolar Disorder, OCD, anxiety disorders, ADHD, and psychotic disorders. We believe that by providing comprehensive care, we can help our patients heal both emotionally and physically.</p>
    <p>We know that mental health is complex and that multiple factors can contribute to the development of mental illness. For this reason, we take an integrative approach that considers the whole person. We understand that each individual has their own unique set of experiences, strengths, and challenges, and we tailor our treatment plans to suit each patient’s personal needs.</p>
  </div>

  <div class="circuit-art circuit-art--left" role="img" aria-label="Blue circuit-node decoration"></div>
  <div class="circuit-art circuit-art--right" role="img" aria-label="Blue circuit-node decoration"></div>
  <div class="phone">555-014-2290</div>
  <div class="web-pill">WWW.<b>VARENPSYCHIATRY</b>.COM</div>
</section>

<section class="flyer flyer--back">
  <div class="tms-photo" role="img" aria-label="Patient receiving transcranial magnetic stimulation with a coil held to her head"></div>
  <div class="body-copy body-copy--intro">
    <p>So often, when we think about mental health, we focus on just treating symptoms. If someone is depressed, they might take medication to help them feel better. If someone is anxious, they might see a therapist to help them manage their anxiety. While these treatments can be helpful, they only address the symptoms of mental illness. To truly address mental health, it is necessary to treat the root causes. This might involve addressing childhood trauma, unresolved conflict, or feelings of worthlessness. It might also involve developing healthy coping mechanisms and learning how to set boundaries. By treating the root causes of mental illness, we can begin to create lasting change.</p>
  </div>
  <div class="body-copy body-copy--plan">
    <p>Our personalized psychiatry plan includes a bio-psycho-social evaluation, tailored treatment plan, medical evaluation for underlying hormonal and electrolyte abnormalities, and genetic testing (when warranted). Our integrative psychiatry approach combines cutting edge, evidence-based treatments with holistic therapies to provide you with the best possible care. In addition, we also offer Ketamine Assisted Therapy, TMS (Transcranial Magnetic Simulation), and MAT Treatment for Substance abuse. We pride ourselves on always staying up to date on the latest mental health treatments.</p>
  </div>

  <div class="about-card">
    <p class="about-card__text">Dr. Tom Pim is a psychiatrist with years of experience providing compassionate, evidence-based care to patients of all ages. He is uniquely trained in several cutting-edge treatments, including Ketamine, Transcranial Magnetic Stimulation (TMS), and integrative psychiatry. Prior to founding Varen Psychiatry, Dr. Pim served as Chief Resident at the largest private psychiatry hospital in Colorado. While there, he won three consecutive awards for exceptionally high Psychiatry in-service test scores (99th percentile). In addition, he was a board member of the Westfield Psychiatric Guild and helped advocate for better Colorado mental health policy. Thanks to his extensive training and experience, Dr. Pim is able to provide each patient with an individualized treatment plan that brings optimum results.</p>
  </div>
  <div class="portrait-ring">
    <div class="portrait" role="img" aria-label="Black and white portrait of Dr. Tom Pim"></div>
  </div>

  <div class="logo-lockup logo-lockup--back">
    <span class="logo-lockup__dot"></span>
    <span class="logo-lockup__name">Varen Psychiatry</span>
  </div>
  <div class="phone">CALL US: <b>555-014-2290</b></div>
  <div class="web-pill">WWW.<b>VARENPSYCHIATRY</b>.COM</div>

  <div class="circuit-art circuit-art--left" role="img" aria-label="Blue circuit-node decoration"></div>
  <div class="circuit-art circuit-art--right" role="img" aria-label="Blue circuit-node decoration"></div>
</section>

</body>
</html>
```